New Business Card Design Project

We are looking for a talented individual to create a truly awesome/unique business card design for us. We are looking for a someone to design something that will really stand out from the crowd - we don't mind what ideas you come up with (ie embossed/flat/matte/shine etc etc) just wow us with your creativity.
Updates

Target Market(s)

Video Games Industry Professionals (all levels of seniority from QA Testers through to CEOs)

Contact Information for Business Card

Company logo (see upload)
Company name: Northbay Play Careers Ltd
Employee Name: Darren Elsby
Job title: CEO
Website: www.nbpc2go.example
Office +44 1632 960418
Mobile: +44 7700 900276
Email: darren@nbpc2go.example

Colors

Designer to choose colors to be used in the design.

Requirements
Must have
• The business card design MUST contain all the information listed in the BUSINESS CARD DETAILS box.
• You will see the colours that are relevant to us (ie company logo) in the uploaded imagery - however you do not have to use all these colours when designing the business card itself
• MUST BE DOUBLE SIDED

```html
<!DOCTYPE html>
<html lang="en">
<head>
<meta charset="utf-8">
<title>Northbay Play Careers – Business Card</title>
<link rel="stylesheet" href="https://fonts.googleapis.com/css2?family=Exo+2:wght@500;700&family=Open+Sans:wght@400;600&display=swap">
<style>
  :root {
    --backdrop: #8c8c8c;
    --card-light: #eeeeee;
    --navy: #1c2f6b;
    --orange: #f07c1e;
    --ink: #1a1a1a;
    --rule: #555555;
    --white: #ffffff;
  }
  * { margin: 0; padding: 0; box-sizing: border-box; }
  html, body { width: 1200px; height: 1200px; overflow: hidden; }
  body { background: var(--backdrop); position: relative; font-family: "Open Sans", sans-serif; }

  .card { position: absolute; top: 310px; height: 594px; box-shadow: 0 3px 6px rgba(0,0,0,.35); }
  .card-front { left: 234px; width: 364px; background: var(--card-light); }
  .card-back { left: 627px; width: 370px; background: var(--navy); }

  .brand-mark { position: absolute; left: 52px; top: 140px; display: flex; align-items: center; gap: 12px; }
  .brand-dot { width: 36px; height: 36px; border-radius: 50%; background: var(--navy); flex: none; }
  .brand-name { font-family: "Exo 2", sans-serif; font-weight: 700; font-size: 24px; line-height: 1.05; color: var(--navy); }

  .person { position: absolute; left: 0; right: 0; top: 338px; text-align: center; }
  .person-name { font-family: "Exo 2", sans-serif; font-weight: 500; font-size: 28px; color: var(--navy); line-height: 1; }
  .person-title { font-size: 15px; color: var(--orange); margin-top: 6px; letter-spacing: .5px; }

  .icon-row { position: absolute; left: 71px; width: 223px; top: 403px; display: flex; align-items: center; gap: 5px; }
  .icon-row .rule { flex: 1; height: 1px; background: var(--rule); }
  .icon-row .rule:first-child { margin-right: 5px; }
  .icon-row .rule:last-child { margin-left: 5px; }
  .icon { width: 22px; height: 22px; border-radius: 4px; background: var(--navy); display: flex; align-items: center; justify-content: center; }
  .icon svg { width: 14px; height: 14px; }

  .contact-list { position: absolute; left: 0; right: 0; top: 434px; list-style: none; text-align: center; font-size: 19px; line-height: 26.5px; color: var(--ink); }

  .back-name { position: absolute; left: 0; right: 0; top: 395px; text-align: center; font-family: "Exo 2", sans-serif; font-weight: 700; font-size: 40px; line-height: 1.05; color: var(--white); }
  .back-web { position: absolute; left: 0; right: 0; top: 523px; text-align: center; font-size: 19px; font-weight: 600; color: var(--white); }
</style>
</head>
<body>
  <section class="card card-front">
    <div class="brand-mark">
      <span class="brand-dot"></span>
      <span class="brand-name">Northbay Play<br>Careers</span>
    </div>

    <div class="person">
      <p class="person-name">Darren Elsby</p>
      <p class="person-title">CEO</p>
    </div>

    <div class="icon-row">
      <span class="rule"></span>
      <span class="icon"><svg viewBox="0 0 16 16"><path fill="#fff" d="M4 1l2.5 3-1.5 1.6c.8 1.9 2.4 3.5 4.3 4.4L11 8.5l3 2.5-1.5 3C7 14 2 9 2 3.5z"/></svg></span>
      <span class="icon"><svg viewBox="0 0 16 16"><rect x="4" y="1" width="8" height="14" rx="1.5" fill="none" stroke="#fff" stroke-width="1.6"/><circle cx="8" cy="12.3" r="1" fill="#fff"/></svg></span>
      <span class="icon"><svg viewBox="0 0 16 16"><rect x="1.5" y="3.5" width="13" height="9" fill="none" stroke="#fff" stroke-width="1.5"/><path d="M1.5 3.5L8 9l6.5-5.5" fill="none" stroke="#fff" stroke-width="1.5"/></svg></span>
      <span class="icon"><svg viewBox="0 0 16 16"><circle cx="8" cy="8" r="6.2" fill="none" stroke="#fff" stroke-width="1.5"/><path d="M2 8h12M8 1.8c2.2 2 2.2 10.4 0 12.4M8 1.8c-2.2 2-2.2 10.4 0 12.4" fill="none" stroke="#fff" stroke-width="1.1"/></svg></span>
      <span class="rule"></span>
    </div>

    <ul class="contact-list">
      <li>+44 1632 960418</li>
      <li>+44 7700 900276</li>
      <li>darren@nbpc2go.example</li>
      <li>www.nbpc2go.example</li>
    </ul>
  </section>

  <section class="card card-back">
    <p class="back-name">Northbay Play<br>Careers</p>
    <p class="back-web">www.nbpc2go.example</p>
  </section>
</body>
</html>
```